Maple Cove Laser Dermal Studio needs an 8 page WP redesign

We need a colorful re-design for an 8 page Wordpress website. The current preliminary website is live. The home page URL is http://maplecovelaserdermalstudio.com The new logo is live on the website also. I would like a (re)design using the colors that are represented by the new logo file, and any additional complimentary colors. The information regarding the business can be found on the website already, so please review it for insight. The name of the business is "Maple Cove Laser Dermal Studio".

Target Market(s)

The targeted website viewer is an adult female between the ages of 30 and 75 who is interested in facial renewal, wart removal and scar removal. This website should inspire in the target viewer the benefits of laser facial renewal, wart removal and new scar removal. Potential website viewers are wanting and searching for improved skin health and appearance. The website must represent the essence of a professional spa business.

Industry/Entity Type

Business

Font styles to use
Sans Serif

Requirements
Must have
• - The phone number placed in a visible and high value widget area that allows mobile phone browser dialing.

```html
<!DOCTYPE html>
<html lang="en">
<head>
<meta charset="utf-8">
<title>Maple Cove Laser Dermal Studio</title>
<link rel="stylesheet" href="https://fonts.googleapis.com/css2?family=Open+Sans:wght@400;600;700&display=swap">
<style>
:root{
  --pink:#c2185b;
  --pink-light:#e0407e;
  --ink:#333;
  --muted:#666;
  --grey-band:#efefef;
  --footer:#2b2b2b;
  --white:#fff;
}
*{margin:0;padding:0;box-sizing:border-box}
html,body{width:882px;height:1200px;overflow:hidden}
body{font-family:"Open Sans",Arial,sans-serif;color:var(--ink);background:var(--white);position:relative}
.header{position:absolute;left:0;top:0;width:882px;height:240px}
.hero-photo{position:absolute;left:0;top:0;width:882px;height:240px;
  background:linear-gradient(90deg,#f4f1f2 0%,#e9dcdc 35%,#c99a96 60%,#7c3a4a 80%,#3c2430 100%)}
.brand{position:absolute;left:30px;top:12px;display:flex;align-items:center;gap:8px}
.brand-mark{width:14px;height:14px;border-radius:50%;background:var(--pink)}
.brand-name{font-size:15px;font-weight:700;color:var(--pink);width:150px;line-height:1.15}
.call{position:absolute;right:30px;top:14px;font-size:17px;font-weight:700;color:var(--pink);display:flex;align-items:center;gap:6px}
.call a{color:var(--white);text-decoration:none}
.call span{color:var(--white)}
.nav{position:absolute;left:200px;top:48px;display:flex;gap:3px}
.nav a{font-size:11px;color:var(--white);text-decoration:none;padding:6px 11px;background:rgba(60,30,40,.55)}
.nav a.active{background:var(--pink)}
.intro{position:absolute;left:53px;top:248px;width:785px}
.intro h1{font-size:21px;font-weight:400;color:var(--pink);margin-bottom:10px}
.intro p{font-size:10px;line-height:1.6;color:var(--muted);margin-bottom:8px}
.treatment-photo{position:absolute;left:53px;top:432px;width:388px;height:206px;
  background:linear-gradient(135deg,#f3e3da,#d9b8a8 55%,#9d8c8c)}
.play{position:absolute;left:50%;top:50%;transform:translate(-50%,-50%)}
.special{position:absolute;left:465px;top:432px;width:373px;height:206px;background:#f6f6f6}
.special h2{background:var(--pink);color:var(--white);font-size:15px;font-weight:600;padding:7px 12px;letter-spacing:.3px}
.special ul{list-style:none;padding:10px 14px}
.special li{font-size:10px;color:var(--muted);line-height:1.5;margin-bottom:5px;padding-left:14px;position:relative}
.special li::before{content:"";position:absolute;left:0;top:4px;width:6px;height:6px;background:var(--pink)}
.band{position:absolute;left:0;top:660px;width:882px;height:432px;background:var(--grey-band)}
.band h2{font-size:18px;font-weight:400;color:var(--pink);position:absolute;top:22px}
.gallery-title{left:53px}
.testimonial-title{left:500px}
.gallery-item{position:absolute;top:64px;width:182px}
.gallery-photo{width:182px;height:140px;background:radial-gradient(circle at 50% 45%,#f1ddd2,#d8bfb4 60%,#fafafa)}
.gallery-item p{font-size:10px;color:var(--muted);line-height:1.5;margin:10px 0 8px}
.btn{display:inline-block;font-size:9px;color:var(--white);background:var(--pink);padding:4px 10px;text-decoration:none}
.testimonial{position:absolute;left:500px;top:64px;width:338px;background:var(--white);padding:14px 16px;border:1px solid #ddd}
.testimonial p{font-size:10px;color:var(--muted);line-height:1.6}
.quote{font-size:28px;color:var(--pink);line-height:.6;font-weight:700}
.author{position:absolute;left:500px;top:256px;display:flex;align-items:center;gap:12px}
.avatar{width:54px;height:54px;border-radius:50%;background:linear-gradient(#d9c3b8,#a98a7e)}
.author strong{display:block;font-size:11px;color:var(--ink)}
.author small{font-size:9px;color:var(--muted)}
.footer{position:absolute;left:0;top:1108px;width:882px;height:92px;background:var(--footer)}
.footer nav{position:absolute;left:53px;top:22px;display:flex;gap:6px}
.footer nav a{font-size:10px;color:#ddd;text-decoration:none}
.footer nav span{font-size:10px;color:#888}
.copyright{position:absolute;left:53px;top:48px;font-size:9px;color:#aaa}
.footer .brand{left:auto;right:40px;top:26px}
.footer .brand-name{color:var(--pink-light)}
</style>
</head>
<body>
<header class="header">
  <div class="hero-photo" role="img" aria-label="Close-up portrait of a woman with smooth skin and red lipstick"></div>
  <div class="brand"><span class="brand-mark"></span><span class="brand-name">Maple Cove Laser Dermal Studio</span></div>
  <div class="call">
    <svg width="16" height="16" viewBox="0 0 24 24" aria-hidden="true"><path fill="#c2185b" d="M6.6 10.8a15.1 15.1 0 0 0 6.6 6.6l2.2-2.2a1 1 0 0 1 1-.25 11.4 11.4 0 0 0 3.6.57 1 1 0 0 1 1 1V20a1 1 0 0 1-1 1A17 17 0 0 1 3 4a1 1 0 0 1 1-1h3.5a1 1 0 0 1 1 1 11.4 11.4 0 0 0 .57 3.6 1 1 0 0 1-.25 1z"/></svg>
    CALL : <a href="tel:8885553376">888-555-DERM (3376)</a>
  </div>
  <nav class="nav">
    <a class="active" href="#">Home</a><a href="#">About Us</a><a href="#">Skin Renewal</a><a href="#">Scar Removal</a><a href="#">Wart Removal</a><a href="#">Your Visit</a><a href="#">Contact Us</a><a href="#">Blog</a>
  </nav>
</header>

<section class="intro">
  <h1>Have you considered Laser Skin Renewal Therapy?</h1>
  <p>Based in Maple Cove, our studio was founded to bring gentle, modern laser care to every client. We combine proven dermal technology with a calm spa setting, so each visit feels relaxing. Our trained team offers skin renewal, scar removal and wart removal treatments tailored to your skin type and goals, helping you look fresh and feel confident every day.</p>
  <p>Since opening, we have served many happy clients with safe and effective laser care. Every session begins with a friendly consultation to explain your options and expected results. We use trusted equipment and follow careful safety steps, giving you a comfortable experience and lasting improvement in tone, texture and clarity of your skin.</p>
</section>

<div class="treatment-photo" role="img" aria-label="Video still of a woman receiving a facial laser treatment">
  <svg class="play" width="44" height="44" viewBox="0 0 44 44" aria-hidden="true"><circle cx="22" cy="22" r="21" fill="rgba(255,255,255,.8)"/><path d="M17 13l14 9-14 9z" fill="#c2185b"/></svg>
</div>

<aside class="special">
  <h2>NEW YEAR RESOLUTION SPECIAL !</h2>
  <ul>
    <li>Restore Your Youthful Skin this Year!</li>
    <li>Take advantage of our laser skin renewal specials for single or multiple sessions at low pricing</li>
    <li>Special ENDS January 31, 2015 at 5:00 PM</li>
    <li>1 Single Session Deal - $149</li>
    <li>3 Sessions Package Deal - $349</li>
    <li>5 Sessions Package Deal - $499</li>
  </ul>
</aside>

<section class="band">
  <h2 class="gallery-title">OUR GALLERY</h2>
  <div class="gallery-item" style="left:53px">
    <div class="gallery-photo" role="img" aria-label="Portrait of a woman with radiant skin"></div>
    <p>Lorem ipsum dolor sit amet, consectetur adipiscing elit, sed do eiusmod tempor incididunt ut labore et dolore</p>
    <a class="btn" href="#">Read More</a>
  </div>
  <div class="gallery-item" style="left:280px">
    <div class="gallery-photo" role="img" aria-label="Portrait of a woman touching her smooth face"></div>
    <p>Lorem ipsum dolor sit amet, consectetur adipiscing elit, sed do eiusmod tempor incididunt ut labore et dolore</p>
    <a class="btn" href="#">Read More</a>
  </div>

  <h2 class="testimonial-title">TESTIMONIALS</h2>
  <blockquote class="testimonial">
    <div class="quote">&ldquo;</div>
    <p>Lorem ipsum dolor sit amet, consectetur adipiscing elit. Donec id ligula et nisi commodo consequat. Duis aute irure dolor in reprehenderit in voluptate velit esse cillum dolore eu fugiat nulla pariatur. Excepteur sint occaecat cupidatat non proident, sunt in culpa qui officia deserunt mollit anim id est laborum. Sed ut perspiciatis unde omnis iste natus error sit voluptatem.</p>
  </blockquote>
  <div class="author">
    <div class="avatar" role="img" aria-label="Client portrait"></div>
    <div><strong>-Jane Porter</strong><small>Client, Maple Cove</small></div>
  </div>
</section>

<footer class="footer">
  <nav>
    <a href="#">Home</a><span>|</span><a href="#">About Us</a><span>|</span><a href="#">Skin Renewal</a><span>|</span><a href="#">Scar Removal</a><span>|</span><a href="#">Wart Removal</a><span>|</span><a href="#">Your Visit</a><span>|</span><a href="#">Contact Us</a><span>|</span><a href="#">Blog</a>
  </nav>
  <p class="copyright">Copyright &copy; 2014 All Rights Reserved | Privacy Policy</p>
  <div class="brand"><span class="brand-mark"></span><span class="brand-name">Maple Cove Laser Dermal Studio</span></div>
</footer>
</body>
</html>
```